Webdesign für Online-Shop für Honig
Zielgruppe
Verkauf von Sidr Honig. Ein sehr hochwertiger Premium-Honig aus dem Jemen.
Aufgabenstellung
Zu Erstellen ist ein Design für einen Onlineshop. Der Onlineshop verkauft Kosmetik-, Lebensmittel- und Gesundheitsprodukte die alle auf einem Honig basieren.
Domain: qalvenu.com
Die Seite soll sehr hochwertig und orientalisch wirken. Der Hintergrund soll auf jeden Fall dunkel sein.
Wir benötigen ein Screendesign der:
- Home-Seite,
- Über uns-Seite
- Produktdetailseite.
Die Designs müssen nicht per HTML umgesetzt werden, können aber. Es reicht ein reines Design als Bild, HTML ist aber auch in Ordnung.
Bitte hochwertige Stockbilder nutzen.

```html
<!DOCTYPE html>
<html lang="de">
<head>
<meta charset="utf-8">
<title>Qalvenu – Produktdetailseite</title>
<link rel="stylesheet" href="https://fonts.googleapis.com/css2?family=Great+Vibes&family=Roboto:wght@400;500&family=Roboto+Slab:wght@300;400&display=swap">
<style>
:root{
  --dark:#2b231e;
  --dark-2:#241d19;
  --gold:#c8914f;
  --gold-soft:#dcb07c;
  --white:#ffffff;
  --ink:#1f1a17;
}
*{margin:0;padding:0;box-sizing:border-box}
html,body{width:1200px;height:2269px;overflow:hidden}
body{position:relative;background:var(--white);font-family:'Roboto',sans-serif;color:var(--ink)}
.abs{position:absolute}

/* header */
.site-header{left:0;top:0;width:1200px;height:98px;background:var(--dark)}
.drip{left:120px;top:0;width:14px;height:36px;background:var(--gold);border-radius:0 0 7px 7px}
.nav a{position:absolute;top:44px;color:var(--gold);font-size:18px;letter-spacing:1px;text-decoration:none;font-weight:400}
.brand{position:absolute;left:0;width:1200px;text-align:center;top:26px;color:var(--gold);font-family:'Roboto Slab',serif;font-weight:300;font-size:34px;letter-spacing:2px;line-height:1}
.brand-sub{position:absolute;left:0;width:1200px;text-align:center;top:71px;color:var(--gold);font-size:10px;letter-spacing:3px}
.cart{left:1119px;top:35px;width:37px;height:37px;border:1.5px solid var(--gold)}

/* breadcrumb */
.breadcrumb{left:100px;top:122px;font-size:13px;color:var(--gold-soft)}
.breadcrumb b{font-weight:400;color:var(--gold)}

/* product */
.product-photo{left:100px;top:198px;width:367px;height:385px;background:linear-gradient(135deg,#4a4039,#2a221e 60%,#1c1714);border-radius:6px}
.ornament-bg{left:720px;top:490px;width:480px;height:397px;background:radial-gradient(ellipse at 70% 50%,#f8f1e8,#ffffff 70%)}
.product-name{left:537px;top:258px;font-family:'Roboto Slab',serif;font-weight:300;font-size:39px;color:var(--gold);letter-spacing:1px;line-height:1.2}
.dots{border-top:3px dotted var(--gold)}
.price{left:537px;top:330px;font-size:28px;font-weight:400;color:var(--gold);font-family:'Roboto',sans-serif}
.lead{left:537px;top:382px;width:320px;font-size:12.5px;line-height:18px}
.label{font-size:17px;letter-spacing:1.5px;color:var(--gold)}
.btn{border:1.5px solid var(--gold);padding:3px}
.btn span{display:block;background:var(--gold);color:var(--white);height:100%;text-align:center;font-size:17px;letter-spacing:1px;line-height:45px;font-weight:400}

.tabs{left:100px;top:655px;font-family:'Roboto Slab',serif;font-size:19px;font-weight:300;color:var(--gold);letter-spacing:1px}
.tab-line{left:100px;top:684px;width:77px;height:3px;background:var(--gold)}
.details{left:100px;top:716px;width:1000px;font-size:13px;line-height:18.3px}
.details p+p{margin-top:18px}

/* other products */
.other{left:0;top:887px;width:1200px;height:708px;background:var(--dark)}
.side-pattern{top:1000px;width:100px;height:595px;background:linear-gradient(180deg,#322822,#2e251f)}
.section-title{left:0;width:1200px;top:943px;text-align:center;color:var(--white);font-family:'Roboto Slab',serif;font-weight:300;font-size:25px;letter-spacing:1px}
.card{top:1035px;width:308px;height:507px;background:var(--white)}
.badge{position:absolute;left:25px;top:25px;width:70px;height:43px;border:1px solid var(--gold);color:var(--gold);font-size:18px;text-align:center;line-height:41px}
.card-photo{position:absolute;left:81px;top:84px;width:147px;height:297px;background:linear-gradient(90deg,#1a1614,#3a302a 45%,#141110);border-radius:30px 30px 18px 18px}
.card-price{position:absolute;top:405px;font-size:18px;color:var(--gold-soft)}
.card-name{position:absolute;left:25px;top:437px;font-size:18px;line-height:23px;letter-spacing:1px;color:var(--gold)}
.card-add{position:absolute;left:215px;top:436px;width:70px;height:43px;background:var(--gold);color:var(--white);font-size:18px;text-align:center;line-height:43px;letter-spacing:.5px}

/* banner */
.banner{left:0;top:1595px;width:1200px;height:415px;background:linear-gradient(90deg,rgba(40,28,20,.55),rgba(40,28,20,0) 35%),radial-gradient(ellipse at 60% 45%,#7c4a1c,#5a3514 55%,#3e2713)}
.tagline{left:0;top:1740px;width:1200px;text-align:center;font-family:'Great Vibes',cursive;font-size:74px;line-height:1;color:var(--gold);letter-spacing:1px}
.btn-outline{left:516px;top:1859px;width:172px;height:53px;border:1.5px solid var(--gold);padding:3px}
.btn-outline span{display:block;height:100%;border:1px solid var(--gold);color:var(--gold);text-align:center;line-height:43px;font-size:17px;letter-spacing:1.5px}

/* footer */
.site-footer{left:0;top:2010px;width:1200px;height:259px;background:var(--dark)}
.foot-brand{left:91px;top:2155px;width:180px;text-align:center;color:var(--gold);font-family:'Roboto Slab',serif;font-weight:300;font-size:38px;line-height:1}
.foot-brand-sub{left:91px;top:2204px;width:180px;text-align:center;color:var(--gold);font-size:11px;letter-spacing:3px}
.foot-mark{left:154px;top:2060px;width:54px;height:54px;border:2px solid var(--gold);border-radius:50%}
.foot-h{top:2062px;font-family:'Roboto Slab',serif;font-weight:300;font-size:18px;color:var(--gold);letter-spacing:.5px}
.foot-p{top:2106px;width:240px;font-size:13px;line-height:18.3px}
.foot-links{left:957px;top:2106px;font-size:13px;line-height:25px;color:var(--white);list-style:none}
.social{top:2196px;width:22px;height:22px;border:2px solid var(--gold);border-radius:4px}
</style>
</head>
<body>

<header class="abs site-header">
  <div class="abs drip"></div>
  <nav class="nav">
    <a style="left:100px">HOME</a>
    <a style="left:193px">ABOUT US</a>
    <a style="left:323px">HISTORY</a>
    <a style="left:798px">HEALTHY</a>
    <a style="left:925px">BEAUTY</a>
    <a style="left:1036px">TASTY</a>
  </nav>
  <div class="brand">QALVENU</div>
  <div class="brand-sub">PREMIUM HONEY</div>
  <div class="abs cart">
    <svg width="34" height="34" viewBox="0 0 34 34"><path d="M9 11h3l2 9h9l2-6H13" fill="none" stroke="#c8914f" stroke-width="2"/><circle cx="15" cy="23" r="1.5" fill="#c8914f"/><circle cx="22" cy="23" r="1.5" fill="#c8914f"/></svg>
  </div>
</header>

<div class="abs breadcrumb">Home | <b>Produktdetailseite</b></div>

<div class="abs ornament-bg" role="img" aria-label="Faint oriental ornament decoration"></div>
<div class="abs product-photo" role="img" aria-label="Dark honey jar with matching gift box"></div>

<h1 class="abs product-name" style="font-weight:300">PRODUCT NAME</h1>
<div class="abs dots" style="left:537px;top:315px;width:137px"></div>
<div class="abs price">0,00 €</div>
<p class="abs lead">Licae as nimoditatium quod quibus desed que num iderionseque la il et earis es entusto tatioss ectatur, offictur accatur epreiumetur.</p>
<div class="abs label" style="left:537px;top:453px">SIZE</div>
<div class="abs" style="left:657px;top:456px;font-size:13px">150 g</div>
<div class="abs label" style="left:537px;top:484px">QUANTITY</div>
<div class="abs" style="left:662px;top:485px;font-size:14px;color:var(--gold)">-</div>
<div class="abs" style="left:683px;top:486px;font-size:13px">1</div>
<div class="abs" style="left:704px;top:484px;font-size:16px;color:var(--gold)">+</div>
<div class="abs btn" style="left:537px;top:526px;width:172px;height:53px"><span>SHOP NOW</span></div>

<div class="abs tabs"><span>DETAILS</span><span style="margin-left:56px">OPTION</span></div>
<div class="abs tab-line"></div>
<div class="abs details">
  <p>Licae as nimoditatium quod quibus desed que num iderionseque la il et earis es entusto tatioss ectatur, offictur accatur epreiumetur.</p>
  <p>Uciusa quo maion con nost vendite cuscil molorio nsequatem fugit laborion comnim fuga. Rit haribus, aut estia et optata nullab inum quatur, si quid untiasperum idel maio. Iberend aepelenet voles dolo moles volupti oremolore quas dolum et fugitate volecte conse ad quassit essequi sam alit aliquas atem es este porro bero volupita volorpos sitatem. Ant diorios everehenda inusdam dus, arcit voloris alit andae. Git as eum repuda quias andebis simpor aut re lam doluptur milliberum arum facimus santi doluptae quas minciam eatiae vendica tusdanis re laceario idis rae et, officiae vent ide porrum apis et et, solestia cus alibus nempora ipita aborempos aut et inci to.</p>
</div>

<section class="abs other"></section>
<div class="abs side-pattern" style="left:0" role="img" aria-label="Dark ornamental pattern"></div>
<div class="abs side-pattern" style="left:1100px" role="img" aria-label="Dark ornamental pattern"></div>
<h2 class="abs section-title" style="font-weight:300">OTHER PRODUCTS</h2>
<div class="abs dots" style="left:540px;top:982px;width:120px;border-top-color:var(--white)"></div>

<article class="abs card" style="left:100px">
  <div class="badge">NEW</div>
  <div class="card-photo" role="img" aria-label="Dark glass honey jar"></div>
  <div class="card-price" style="left:25px">0,00 €</div>
  <div class="card-price" style="right:27px">150 g</div>
  <div class="card-name">PRODUCT<br>NAME</div>
  <div class="card-add">ADD</div>
</article>
<article class="abs card" style="left:446px">
  <div class="badge">NEW</div>
  <div class="card-photo" role="img" aria-label="Dark glass honey jar"></div>
  <div class="card-price" style="left:25px">0,00 €</div>
  <div class="card-price" style="right:27px">150 g</div>
  <div class="card-name">PRODUCT<br>NAME</div>
  <div class="card-add">ADD</div>
</article>
<article class="abs card" style="left:792px">
  <div class="badge">NEW</div>
  <div class="card-photo" role="img" aria-label="Dark glass honey jar"></div>
  <div class="card-price" style="left:25px">0,00 €</div>
  <div class="card-price" style="right:27px">150 g</div>
  <div class="card-name">PRODUCT<br>NAME</div>
  <div class="card-add">ADD</div>
</article>

<div class="abs banner" role="img" aria-label="Close-up photo of golden honeycomb"></div>
<p class="abs tagline">Beauty · Healthy · Tasty</p>
<div class="abs btn-outline"><span>SHOW MORE</span></div>

<footer class="abs site-footer"></footer>
<div class="abs foot-mark"></div>
<div class="abs foot-brand">QALVENU</div>
<div class="abs foot-brand-sub">PREMIUM HONEY</div>

<h3 class="abs foot-h" style="left:359px;font-weight:300">HEADLINE 3</h3>
<p class="abs foot-p" style="left:359px;color:var(--gold)">Licae as nimoditatium quod quibus desed que num iderionseque la il et earis es entusto tatioss ectatur, offictur Upid explaccum quiasitia nobitibus</p>
<div class="abs social" style="left:360px"></div>
<div class="abs social" style="left:395px"></div>
<svg class="abs" style="left:428px;top:2196px" width="28" height="22" viewBox="0 0 28 22"><rect x="1" y="1" width="26" height="20" rx="3" fill="none" stroke="#c8914f" stroke-width="2"/><path d="M2 3l12 9 12-9" fill="none" stroke="#c8914f" stroke-width="2"/></svg>

<h3 class="abs foot-h" style="left:659px;font-weight:300">HEADLINE 3</h3>
<p class="abs foot-p" style="left:659px;color:var(--white)">Licae as nimoditatium quod quibus desed que num iderionseque la il et earis es entusto tatioss ectatur, offictur Upid explaccum quiasitia nobitibus</p>

<h3 class="abs foot-h" style="left:957px;font-weight:300">HEADLINE 3</h3>
<ul class="abs foot-links"><li>Datenschutz</li><li>Impressum</li><li>AGB</li></ul>

</body>
</html>
```